Design for Certificate

Design a certificate for training, providing our company logo such as attachments. Company's name is "ØSTRA Velmark Advisory Ltd", please refer to our company profile: https://www.ostra-velmark.example/company_info

The style of the current certificate is also attached, and another certificate of another company can be referred to. Psd & jpg are required for the final draft (the layers of psd are not merged). Thanks!

```html
<!DOCTYPE html>
<html lang="en">
<head>
<meta charset="utf-8">
<title>ØSTRA Velmark Advisory Ltd — Certificate and Business Cards</title>
<link rel="stylesheet" href="https://fonts.googleapis.com/css2?family=Tinos:wght@400;700&family=Noto+Sans+TC:wght@400&display=swap">
<style>
  :root {
    --backdrop: #ebe8e8;
    --charcoal: #4a4a4c;
    --rose: #e2b9a1;
    --rose-deep: #d9a98e;
    --paper: #f8f7f7;
    --mat: #dcd7d6;
    --ink: #1c1c1c;
    --ink-soft: #555555;
    --faint: #e4e1e0;
    --card-white: #ffffff;
  }
  * { box-sizing: border-box; margin: 0; padding: 0; }
  html, body { width: 1200px; height: 1000px; overflow: hidden; }
  body {
    position: relative;
    background: var(--backdrop);
    font-family: "Tinos", "Times New Roman", serif;
    color: var(--ink);
  }
  .abs { position: absolute; }
  .center { text-align: center; }

  /* ---------- Business card: front ---------- */
  .card {
    position: absolute;
    left: 83px;
    width: 300px;
    height: 182px;
    overflow: hidden;
  }
  .card-front { top: 312px; background: var(--card-white); }
  .card-front .band {
    position: absolute; left: 0; top: 0; width: 100%; height: 70px;
    background: var(--charcoal);
  }
  .card-front .brand-mark {
    position: absolute; left: 0; width: 100%; top: 22px;
    font-size: 20px; letter-spacing: 2px; color: var(--rose); text-align: center;
  }
  .card-front .company {
    position: absolute; left: 0; width: 100%; top: 50px;
    font-size: 8px; color: var(--rose); text-align: center;
  }
  .card-front .emblem-frame {
    position: absolute; left: 214px; top: 2px; width: 80px; height: 116px;
    border: 1px solid rgba(226,185,161,0.45);
  }
  .card-front .holder {
    position: absolute; left: 0; width: 100%; top: 89px;
    font-size: 12px; color: var(--ink-soft); text-align: center;
  }
  .card-front .holder .zh { font-family: "Noto Sans TC", sans-serif; margin-left: 8px; }
  .card-front .role {
    position: absolute; left: 0; width: 100%; top: 104px;
    font-size: 9px; color: var(--ink-soft); text-align: center;
  }
  .card-front .role .zh { font-family: "Noto Sans TC", sans-serif; margin-left: 3px; }
  .card-front .phones {
    position: absolute; left: 0; width: 100%; top: 128px;
    font-size: 8px; color: var(--ink-soft); text-align: center;
  }
  .card-front .address {
    position: absolute; left: 0; width: 100%; top: 144px;
    font-family: "Noto Sans TC", sans-serif; font-size: 10px; color: var(--rose-deep); text-align: center;
  }
  .card-front .email {
    position: absolute; left: 0; width: 100%; top: 160px;
    font-size: 8px; color: var(--ink-soft); text-align: center;
  }

  /* ---------- Business card: back ---------- */
  .card-back { top: 536px; background: var(--charcoal); }
  .card-back .brand-mark {
    position: absolute; left: 0; width: 100%; top: 52px;
    font-size: 36px; letter-spacing: 3px; color: var(--rose); text-align: center;
  }
  .card-back .pronounce {
    position: absolute; left: 0; width: 100%; top: 100px;
    font-family: "Noto Sans TC", sans-serif; font-size: 14px; letter-spacing: 1px;
    color: var(--rose); text-align: center;
  }
  .card-back .site {
    position: absolute; left: 0; width: 100%; top: 121px;
    font-family: "Tinos", serif; font-size: 10px; color: var(--rose); text-align: center;
  }

  /* ---------- Certificate ---------- */
  .certificate-mat {
    position: absolute; left: 455px; top: 57px; width: 627px; height: 885px;
    background: var(--mat);
  }
  .certificate {
    position: absolute; left: 468px; top: 72px; width: 602px; height: 855px;
    background: var(--paper);
  }
  .certificate .logo-box {
    position: absolute; left: 211px; top: 39px; width: 181px; height: 149px;
    background: var(--charcoal);
    display: flex; align-items: center; justify-content: center;
  }
  .certificate .logo-box span {
    font-size: 44px; letter-spacing: 4px; color: var(--rose); padding-top: 18px;
  }
  .certificate .title {
    position: absolute; left: 0; width: 100%; top: 234px;
    font-size: 28px; text-align: center; color: var(--ink);
  }
  .certificate .line-text {
    position: absolute; left: 0; width: 100%;
    font-size: 14px; text-align: center; color: var(--ink);
  }
  .certificate .rule {
    position: absolute; height: 1px; background: var(--ink-soft);
  }
  .certificate .course strong { font-size: 16px; font-weight: 700; }
  .certificate .watermark-frame {
    position: absolute; left: 212px; top: 503px; width: 180px; height: 280px;
    border: 2px solid var(--faint);
    display: flex; align-items: center; justify-content: center;
  }
  .certificate .watermark-frame span {
    font-size: 40px; letter-spacing: 3px; color: var(--faint);
  }
  .certificate .issuer {
    position: absolute; left: 390px; width: 135px; top: 560px;
    font-size: 16px; font-weight: 700; text-align: center; line-height: 19px;
  }
  .certificate .signature {
    position: absolute; left: 368px; top: 610px; width: 155px; height: 36px;
    background: linear-gradient(90deg, rgba(40,40,40,0.06), rgba(40,40,40,0.12), rgba(40,40,40,0.06));
  }
  .certificate .signer {
    position: absolute; left: 352px; width: 201px; top: 651px;
    font-size: 12px; text-align: center; color: var(--ink);
  }
  .certificate .cert-no {
    position: absolute; left: 49px; top: 818px; font-size: 12px;
  }
</style>
</head>
<body>

  <!-- Business card: front -->
  <section class="card card-front" aria-label="Business card front">
    <div class="band"></div>
    <div class="emblem-frame"></div>
    <div class="brand-mark">ØSTRA</div>
    <div class="company">ØSTRA Velmark Advisory Ltd</div>
    <div class="holder">mr Marco Velluti<span class="zh">馬可·維魯提</span></div>
    <div class="role">Consultant<span class="zh">顧問</span></div>
    <div class="phones">TW +886 2 2700 1482&nbsp;&nbsp;DK +45 30 12 45 78</div>
    <div class="address">110台北市信義區松仁路88號12樓</div>
    <div class="email">ostra.service@example.com</div>
  </section>

  <!-- Business card: back -->
  <section class="card card-back" aria-label="Business card back">
    <div class="brand-mark">ØSTRA</div>
    <div class="pronounce">用丹麥語發音</div>
    <div class="site">www.ostra-velmark.example</div>
  </section>

  <!-- Certificate -->
  <div class="certificate-mat"></div>
  <main class="certificate" aria-label="Certificate of Completion">
    <div class="logo-box"><span>ØSTRA</span></div>
    <h1 class="title" style="font-weight:400;">Certificate of Completion</h1>
    <p class="line-text" style="top:287px;">This certificate is awarded to</p>
    <div class="rule" style="left:49px; width:504px; top:366px;"></div>
    <p class="line-text" style="top:389px;">has successfully completed</p>
    <p class="line-text course" style="top:424px;"><strong>Brand Reputation Management</strong> Training Course</p>
    <p class="line-text" style="top:459px; left:148px; width:auto; text-align:left;">Sixteen hours,&nbsp; held on</p>
    <div class="rule" style="left:294px; width:158px; top:472px;"></div>

    <div class="watermark-frame"><span>ØSTRA</span></div>

    <div class="issuer">ØSTRA Velmark Advisory Ltd</div>
    <div class="signature" role="img" aria-label="Handwritten signature of the Chief Technology Officer"></div>
    <div class="rule" style="left:352px; width:201px; top:647px;"></div>
    <div class="signer">Chief Technology Officer</div>

    <p class="cert-no">Certificate No.:</p>
    <div class="rule" style="left:137px; width:157px; top:829px;"></div>
  </main>

</body>
</html>
```